Our Kitchen's Pie website

We have a new website designed and we're ready for front end design

Staging server http://staging.ourkitchenspie.example which uses twitter bootstrap 3.* and we’re looking for a flat design that doesn’t go into the typical italian theme.

We need the desktop and mobile view for all of pages.

Homepage:

If you take a look at the homepage of the staging site you will notice the six boxes but we’re not interested in the Latest Tweets, but we do have a Submit Your Recipe, and Special of the Week

However we are happy with the wireframe with the logo in the middle.

This is our current site: http://crustbyteodor.example so we need forest green colors.

Inner Page:

This is our staging inner page template: http://staging.ourkitchenspie.example/page/2 and I imagine the links that are in the footer to also
be represented in the inner file. However;

UI Kit:

Here is the UI kit which has all the types of fields, and html doc types which we need.

http://gridwidgetset.example

Order Flow:

We need the order flow for the entire buying process from the homepage to the checkout screen.

http://staging.ourkitchenspie.example
http://staging.ourkitchenspie.example/order
http://staging.ourkitchenspie.example/menu
http://staging.ourkitchenspie.example/customize/2

Things to think about:

How will we offer upsells
We want to have a pizza builder https://order.ovenbarn.example/site/pizza/builder

Target Market(s)

Pizza lovers

Industry/Entity Type

Builder

Font styles to use
Sans Serif

Colors
9bcb3c

Requirements
Must have
• Call to Action to Order a pizza.
neat / layered *.psd or *.fw.png
WEB SAFE FONTS! We like google fonts.
bootstraps 960 grid
UX
Nice to have
• Integrating sacred geometry creatively and very subtle. Needing new logo meshed with old logo, must talk to you about this
Should not have
• Complicated Backgrounds with gradients. We like flat design.
Typical Italian Theme
Sliders.

```html
<!DOCTYPE html>
<html lang="en">
<head>
<meta charset="utf-8">
<title>Our Kitchen's Pie</title>
<link rel="stylesheet" href="https://fonts.googleapis.com/css2?family=Open+Sans:wght@300;400;600&display=swap">
<style>
:root{
  --green:#2a8f5c;
  --green-dark:#1e6b45;
  --green-text:#1f7a4c;
  --ink:#222;
  --muted:#555;
  --line:#d8d8d8;
  --hero-bg:#f1f2f1;
  --panel-head:#bdbdbd;
  --white:#fff;
}
*{box-sizing:border-box;margin:0;padding:0}
html,body{width:1200px;height:1098px;overflow:hidden;background:var(--white)}
body{position:relative;font-family:"Open Sans",Arial,sans-serif;color:var(--ink)}
a{color:inherit;text-decoration:none}
.abs{position:absolute}

.account{top:5px;right:101px;font-size:13px;color:var(--green-text)}
.nav{top:34px;font-size:13px;font-weight:400;text-transform:uppercase;color:#333;z-index:5}
.nav a{position:absolute;white-space:nowrap;background:var(--white);padding:0 4px;margin-left:-4px}
.double-rule{left:0;width:1200px;height:5px;border-top:2px solid var(--green);border-bottom:1px solid var(--green)}

.hero{left:0;top:70px;width:1200px;height:398px;background:var(--hero-bg)}
.hero-photo{left:180px;top:70px;width:450px;height:398px;background:linear-gradient(160deg,#f4f4f2 0%,#e8e2da 55%,#c98a4a 80%,#a8522a 100%);border-radius:40% 40% 6px 6px}
.brand{left:500px;top:0;width:178px;height:140px;background:var(--white);display:flex;flex-direction:column;align-items:center;justify-content:center;gap:10px;z-index:4}
.brand-mark{width:46px;height:46px;border-radius:50%;background:var(--green)}
.brand-name{font-size:18px;font-weight:600;color:var(--green)}

.cart{top:106px;left:851px;font-size:13px;color:var(--green-text)}
.accolades{left:818px;top:141px;width:281px;height:288px;border:1px solid #cfcfcf;border-radius:5px;background:var(--white);overflow:hidden}
.accolades h2{height:42px;background:var(--panel-head);color:var(--white);font-size:13px;font-weight:400;text-align:center;line-height:42px}
.accolades p{font-size:13px;line-height:18px;color:#333;padding:0 11px}
.accolades .first{margin-top:19px}
.accolades .second{margin-top:23px}
.badge{position:absolute;top:212px;border-radius:6px}
.badge-open{left:22px;width:92px;height:58px;background:#e9d3d3}
.badge-order{left:148px;width:104px;height:44px;top:220px;background:#d5e8dc}

.banner{left:0;top:482px;width:1200px;height:91px;background:var(--green);text-align:center}
.banner h1{font-size:22.5px;font-weight:400;color:var(--white);margin-top:11px}
.banner .hours{font-size:16px;letter-spacing:1px;color:#123a25;margin-top:14px}
.banner .hours b{font-weight:400;color:var(--white)}

.card{top:623px;width:321px}
.card-photo{height:149px;border:1px solid #bbb}
.card h3{font-size:17px;font-weight:600;color:var(--green-dark);text-transform:uppercase;margin-top:6px;letter-spacing:.2px}
.card p{font-size:13px;line-height:19px;color:var(--muted);margin:5px 0 0 2px;letter-spacing:.2px}
.card-date{position:absolute;top:276px;left:1px;font-size:12px;color:var(--green-text)}
.btn-more{position:absolute;top:276px;right:1px;background:var(--green);color:var(--white);font-size:12px;padding:1px 7px 2px}
.card-rule{position:absolute;top:309px;left:2px;right:0;height:4px;border-top:2px solid var(--green);border-bottom:1px solid var(--green)}

.recipe{left:779px;top:623px;width:321px;height:299px;border:1px solid #d4d4d4}
.recipe h3{font-size:17px;font-weight:400;margin:10px 0 0 23px}
.field{position:absolute;left:23px;width:270px;border:1px solid #d4d4d4;font-size:13px;color:#8a8a8a;padding:8px}
.submit{position:absolute;left:23px;top:254px;width:89px;height:32px;background:var(--green);color:var(--white);border:1px solid var(--green-dark);font-size:14px;text-align:center;line-height:30px}
.recipe-rule{left:780px;top:932px;width:319px;height:4px;border-top:2px solid var(--green);border-bottom:1px solid var(--green)}

.footer-rule{left:0;top:993px;width:1200px;height:3px;border-top:1px solid #ccc;border-bottom:1px solid #e4e4e4}
.footer-links{top:1011px;left:0;width:1200px;text-align:center;font-size:13px;color:#333;letter-spacing:.3px}
.footer-links span{margin:0 14px;color:#555}
.social{top:1044px;left:525px;font-size:13px;display:flex;align-items:center;gap:6px}
.social i{display:inline-block;width:22px;height:22px;border-radius:3px}
</style>
</head>
<body>

<div class="abs account"><a href="#">Login</a> | <a href="#">Signup</a></div>
<div class="abs double-rule" style="top:65px"></div>

<section class="abs hero" role="img" aria-label="Light grey pattern of kitchen ingredients"></section>
<div class="abs hero-photo" role="img" aria-label="Smiling chef in a white hat holding a fresh pizza"></div>

<nav class="abs nav" style="left:0;width:1200px">
  <a href="#" style="left:105px">Home</a>
  <a href="#" style="left:195px">Locations</a>
  <a href="#" style="left:317px">Order Online</a>
  <a href="#" style="left:839px">Menu</a>
  <a href="#" style="left:928px">Contact Us</a>
  <a href="#" style="left:1056px">About</a>
</nav>

<a href="#" class="abs brand">
  <span class="brand-mark"></span>
  <span class="brand-name">Our Kitchen's Pie</span>
</a>

<div class="abs cart">Items (0) | Total: 0.00 | <a href="#">Checkout</a></div>

<aside class="abs accolades">
  <h2>RECENT ACCOLADES</h2>
  <p class="first">Since 1956, we've been honored as having the best pizza in Dallas</p>
  <p class="second">Dallas and Lonestar Ledger awarded us the best pizza in Dallas for 2010 as a finalist in Metro Table Magazine this year</p>
  <span class="badge badge-open" role="img" aria-label="Open 365 days per year badge"></span>
  <a href="#" class="badge badge-order" role="img" aria-label="Order online button"></a>
</aside>

<div class="abs double-rule" style="top:468px"></div>

<section class="abs banner">
  <h1>Our Family's Ancient Sicilian Recipe, Passed Down Since the fall of Rome.</h1>
  <p class="hours">WE ARE OPEN <b>365</b> DAYS * &nbsp;&nbsp; Dallas Location</p>
</section>

<div class="abs double-rule" style="top:580px"></div>

<article class="abs card" style="left:100px">
  <div class="card-photo" role="img" aria-label="Sliced pizza with basil on a wicker board" style="background:linear-gradient(135deg,#e6c48a,#c9883f 55%,#7a5226)"></div>
  <h3>Entrees View Our Menu</h3>
  <p>Sed ut perspiciatis unde omnis iste natus error sit voluptatem accusantium doloremque laudantium, totam rem aperiam, eaque ipsa quae ab illo inventore</p>
  <span class="card-date">17.08.2014</span>
  <a href="#" class="btn-more">View More</a>
  <span class="card-rule"></span>
</article>

<article class="abs card" style="left:441px">
  <div class="card-photo" role="img" aria-label="Pizza with tomatoes, olives and herbs on a wooden table" style="background:linear-gradient(135deg,#5a3a28,#b4562c 50%,#d9a04c 75%,#6b8a3a)"></div>
  <h3>Special Of The Week</h3>
  <p>Sed ut perspiciatis unde omnis iste natus error sit voluptatem accusantium doloremque laudantium, totam rem aperiam, eaque ipsa quae ab illo inventore</p>
  <span class="card-date">17.08.2014</span>
  <a href="#" class="btn-more">View More</a>
  <span class="card-rule"></span>
</article>

<form class="abs recipe">
  <h3>Special Of The Week</h3>
  <div class="field" style="top:43px;height:104px">Paste your recipe here</div>
  <div class="field" style="top:152px;height:34px">Name</div>
  <div class="field" style="top:191px;height:34px">Email</div>
  <div class="submit">Submit</div>
</form>
<div class="abs recipe-rule"></div>

<div class="abs footer-rule"></div>
<footer class="abs footer-links">
  <a href="#">Gift Card</a><span>|</span><a href="#">Newsletter</a><span>|</span><a href="#">Coupons</a><span>|</span><a href="#">Jobs</a><span>|</span><a href="#">Specials</a>
</footer>
<div class="abs social">Social <i style="background:#7cc4e6"></i><i style="background:#4a6fb0"></i></div>

</body>
</html>
```